Corvane Solutions Website

Corvane Solutions (CS) provide Analytics & Enterprise Performance Management (EPM) advisory & consultancy services. We are passionate about data and making a difference for our clients by working in partnership with them, helping them on their journey to becoming an Corvane Solution. We deliver insights which give our clients a competitive edge and a much deeper understanding of their organisation.

We need a website which shows who we are, what we do and how we do it.

www.corvane-solutions.com is our very basic website at the moment. We want to completely revamp it with a corporate look

```html
<!DOCTYPE html>
<html lang="en">
<head>
<meta charset="utf-8">
<title>Corvane Solutions</title>
<link href="https://fonts.googleapis.com/css2?family=Montserrat:wght@600;700;800&family=Lato:wght@400;700&display=swap" rel="stylesheet">
<style>
:root{
  --navy:#17384f;
  --navy-deep:#10283a;
  --navy-soft:#2e5673;
  --orange:#f07f23;
  --grey:#dcdcdc;
  --ink:#111;
  --text:#444;
  --white:#fff;
}
html,body{margin:0;padding:0;overflow:hidden;background:var(--white);}
.canvas{position:relative;width:1200px;height:3589px;overflow:hidden;font-family:'Lato',sans-serif;color:var(--ink);}
.abs{position:absolute;}
.heading{font-family:'Montserrat',sans-serif;font-weight:700;margin:0;letter-spacing:.5px;}
.btn{position:absolute;background:var(--orange);color:var(--white);font-family:'Montserrat',sans-serif;font-weight:600;font-size:14px;border-radius:22px;display:flex;align-items:center;justify-content:center;letter-spacing:.3px;}
.layer{position:absolute;left:0;top:0;}

/* header */
.site-header{position:absolute;left:0;top:0;width:1200px;height:66px;background:var(--white);z-index:3;}
.brand{position:absolute;display:flex;align-items:center;gap:10px;font-family:'Montserrat',sans-serif;font-weight:700;color:var(--navy);}
.brand-dot{border-radius:50%;border:5px solid var(--navy);box-sizing:border-box;}
.topbar{position:absolute;left:685px;top:0;width:530px;height:27px;background:var(--navy);border-bottom-left-radius:18px;color:var(--white);font-size:13px;}
.topbar span{position:absolute;top:5px;}
.nav{position:absolute;top:38px;font-size:13px;font-family:'Montserrat',sans-serif;font-weight:600;}
.nav.active{color:var(--orange);}

/* hero */
.hero-photo{position:absolute;left:0;top:66px;width:1200px;height:600px;background:linear-gradient(120deg,#1c3447 0%,#3b4c57 45%,#5b6870 70%,#2a3d4b 100%);}
.hero-text{position:absolute;left:70px;color:var(--white);}
.eyebrow{font-family:'Montserrat',sans-serif;font-weight:600;font-size:23px;color:var(--orange);}
.hero-title{font-family:'Montserrat',sans-serif;font-weight:800;font-size:39px;line-height:54px;}
.hero-sub{font-family:'Montserrat',sans-serif;font-weight:800;font-size:31px;color:var(--orange);}

/* welcome */
.welcome-copy{position:absolute;left:610px;top:760px;width:500px;}
.body{font-size:15.5px;line-height:27px;color:var(--text);}

/* cards */
.card{position:absolute;top:1634px;width:338px;height:306px;border-radius:20px;box-shadow:0 0 0 2px #eee,0 2px 6px rgba(0,0,0,.08);}
.card-inner{position:absolute;left:9px;top:9px;right:9px;bottom:9px;border:2px solid #222;border-radius:18px;overflow:hidden;background:linear-gradient(180deg,#f4f4f4,#e9eaeb);}
.card-inner.featured{background:linear-gradient(180deg,#35607c,#2a4f69);color:var(--white);}
.card-corner{position:absolute;left:0;top:0;width:105px;height:105px;background:var(--orange);clip-path:polygon(0 0,100% 0,0 100%);}
.card-num{position:absolute;left:18px;top:28px;color:var(--white);font-family:'Montserrat',sans-serif;font-weight:700;font-size:26px;}
.card-title{position:absolute;left:30px;right:30px;top:80px;text-align:center;font-family:'Montserrat',sans-serif;font-weight:700;font-size:21px;line-height:28px;}
.card-text{position:absolute;left:40px;right:40px;top:148px;text-align:center;font-size:14.5px;line-height:20.5px;color:#333;}
.featured .card-text{color:#e8eef2;}

/* form */
.field{position:absolute;left:612px;width:381px;background:var(--white);border:1px solid #e3e3e3;box-shadow:0 2px 4px rgba(0,0,0,.08);box-sizing:border-box;padding:12px 14px;font-size:14px;color:#555;}

/* footer */
.foot-head{position:absolute;top:3306px;color:var(--white);font-family:'Lato',sans-serif;font-size:18px;}
.foot-list{position:absolute;color:var(--white);font-size:13px;}
.foot-list div{position:relative;height:31px;padding-left:21px;}
.foot-list div::before{content:"";position:absolute;left:0;top:5px;width:6px;height:6px;border-radius:50%;background:var(--orange);}
.contact-row{position:absolute;left:317px;display:flex;gap:16px;align-items:flex-start;color:var(--white);font-size:13px;line-height:21px;}
.ico{width:28px;height:28px;border-radius:50%;background:var(--orange);flex:none;display:flex;align-items:center;justify-content:center;}
.social{position:absolute;top:3415px;width:38px;height:38px;border-radius:50%;background:var(--white);}
</style>
</head>
<body>
<div class="canvas">

  <!-- hero background and curves -->
  <div class="hero-photo" role="img" aria-label="Photo of a team of colleagues meeting around a table in an office"></div>
  <svg class="layer" width="1200" height="700" viewBox="0 0 1200 700">
    <path d="M0 450 C200 580 400 625 620 622 C850 618 1050 560 1200 505 L1200 700 L0 700Z" fill="var(--orange)"/>
    <path d="M0 474 C250 615 480 640 690 638 C900 632 1080 585 1200 540 L1200 700 L0 700Z" fill="var(--grey)"/>
    <path d="M0 478 C230 620 460 625 650 620 C880 614 1060 630 1200 660 L1200 700 L0 700Z" fill="var(--white)"/>
  </svg>

  <header class="site-header">
    <div class="brand" style="left:72px;top:12px;font-size:15px;line-height:17px;">
      <div class="brand-dot" style="width:44px;height:44px;"></div>
      <div>CORVANE<br>SOLUTIONS</div>
    </div>
    <div class="topbar">
      <span style="left:34px;">✉ info@corvane-solutions.com</span>
      <span style="left:350px;">☎ 01 555 0142</span>
    </div>
    <div class="nav active" style="left:739px;">Home</div>
    <div class="nav" style="left:835px;">Services</div>
    <div class="nav" style="left:946px;">About Us</div>
    <div class="nav" style="left:1063px;">Contact Us</div>
  </header>

  <div class="hero-text" style="top:211px;">
    <div class="eyebrow">WE PROVIDE</div>
    <div class="hero-title">ANALYTICS &amp; ENTERPRISE<br>PERFORMANCE MANAGEMENT</div>
    <div class="hero-sub">ADVISORY &amp; CONSULTANCY SERVICES</div>
  </div>
  <div class="btn" style="left:72px;top:408px;width:122px;height:42px;">CONTACT US</div>

  <!-- welcome -->
  <svg class="abs" style="left:130px;top:685px;" width="400" height="400" viewBox="0 0 400 400">
    <circle cx="200" cy="200" r="189" fill="none" stroke="var(--orange)" stroke-width="2" stroke-dasharray="5 3"/>
    <circle cx="200" cy="200" r="182" fill="none" stroke="var(--orange)" stroke-width="8"/>
    <circle cx="200" cy="200" r="172" fill="var(--white)"/>
    <circle cx="200" cy="200" r="167" fill="#5b6b74"/>
    <circle cx="288" cy="44" r="24" fill="var(--white)"/>
    <circle cx="288" cy="44" r="17" fill="#cfd3d6"/>
  </svg>
  <div class="abs" style="left:167px;top:722px;width:326px;height:326px;border-radius:50%;background:radial-gradient(circle at 40% 50%,#9aa6ad,#4a5a63 70%,#2e3b42);" role="img" aria-label="Photo of hands typing on a laptop with floating analytics charts"></div>
  <div class="welcome-copy">
    <div class="heading" style="font-size:20px;font-weight:600;">WELCOME TO</div>
    <div class="heading" style="font-size:36px;line-height:43px;margin-top:6px;">CORVANE<br>SOLUTIONS</div>
    <p class="body" style="margin:18px 0 0;">CS are a Data Analytics &amp; EPM company, specialising in the implementation and support of Business Intelligence, EPM and Data Analytics business solutions, both in the Cloud and on-premise.</p>
  </div>

  <!-- who we are -->
  <svg class="layer" width="1200" height="1500" viewBox="0 0 1200 1500">
    <path d="M0 1157 C300 1130 700 1080 1000 1100 C1100 1108 1160 1140 1200 1160 L1200 1493 L0 1493Z" fill="var(--navy)"/>
  </svg>
  <div class="heading abs" style="left:0;width:1200px;top:1188px;text-align:center;color:var(--white);font-size:35px;">WHO WE ARE</div>
  <p class="body abs" style="left:270px;width:660px;top:1248px;margin:0;text-align:center;color:#e6edf2;">Corvane Solutions is an exciting start-up in the Data Analytics and EPM space. Founded in 2019, CS specialise in the implementation and support of BI, EPM and Data Analytics business solutions, both in the Cloud and on-premise.</p>
  <div class="btn" style="left:539px;top:1357px;width:122px;height:40px;">READ MORE</div>

  <!-- what we do -->
  <div class="heading abs" style="left:0;width:1200px;top:1562px;text-align:center;font-size:35px;">WHAT WE DO</div>
  <div class="card" style="left:70px;">
    <div class="card-inner" role="img" aria-label="Faint photo of a consultant at work">
      <div class="card-corner"></div><div class="card-num">01</div>
      <div class="card-title">Advise &amp; Architect Services</div>
      <div class="card-text">Helping our customers understand the art of the possible and safeguarding their investments by overseeing implementations.</div>
    </div>
  </div>
  <div class="card" style="left:430px;">
    <div class="card-inner featured" role="img" aria-label="Faint photo of a project team">
      <div class="card-corner"></div><div class="card-num">02</div>
      <div class="card-title">Design &amp;<br>Implement</div>
      <div class="card-text">Working with the project management team, through each stage of the project, with clearly defined deliverables and well exercised plans to deliver them.</div>
    </div>
  </div>
  <div class="card" style="left:790px;">
    <div class="card-inner" role="img" aria-label="Faint photo of support staff">
      <div class="card-corner"></div><div class="card-num">03</div>
      <div class="card-title">Optimise &amp;<br>Manage</div>
      <div class="card-text">Our Managed Services delivers proactive, on-demand support for EPM and Data Analytics environments</div>
    </div>
  </div>

  <!-- how we do it -->
  <svg class="layer" width="1200" height="2600" viewBox="0 0 1200 2600">
    <path d="M0 2018 H1200 V2490 C1000 2600 600 2580 0 2480Z" fill="var(--navy)"/>
    <rect x="645" y="2076" width="438" height="244" fill="#2d6a93"/>
    <rect x="628" y="2170" width="130" height="230" fill="var(--orange)"/>
    <rect x="643" y="2170" width="115" height="215" fill="var(--navy)"/>
  </svg>
  <div class="abs" style="left:690px;top:2140px;width:440px;height:310px;background:linear-gradient(135deg,#3a3f44,#c9ccce 50%,#4b4f53);box-shadow:0 4px 12px rgba(0,0,0,.35);" role="img" aria-label="Photo of hands holding a tablet showing a business dashboard"></div>
  <svg class="abs" style="left:879px;top:2264px;" width="60" height="60" viewBox="0 0 60 60">
    <circle cx="30" cy="30" r="29" fill="#e52421"/>
    <path d="M23 18 L43 30 L23 42Z" fill="var(--white)"/>
  </svg>
  <div class="heading abs" style="left:70px;top:2100px;color:var(--white);font-size:35px;">HOW WE DO IT</div>
  <div class="abs body" style="left:72px;top:2163px;width:500px;color:#e6edf2;">
    <p style="margin:0 0 18px;">Many desktop publishing packages and web page editors now use Lorem Ipsum as their default model text, and a search for 'lorem ipsum' will uncover many web sites still in their infancy. Various versions have evolved over the years, sometimes by accident .</p>
    <p style="margin:0;">Lorem Ipsum is simply dummy text of the printing and typesetting industry. Lorem Ipsum has been the industry's standard dummy text</p>
  </div>
  <div class="btn" style="left:72px;top:2367px;width:122px;height:40px;">READ MORE</div>

  <!-- contact -->
  <div class="abs" style="left:208px;top:2637px;width:193px;height:260px;background:linear-gradient(180deg,#e9ecef,#b9c2ca);box-shadow:0 2px 8px rgba(0,0,0,.2);border:4px solid #fff;" role="img" aria-label="Photo of a person holding a chart report, labelled EPM services"></div>
  <div class="abs" style="left:336px;top:2717px;font-family:'Montserrat',sans-serif;font-weight:600;font-size:12px;line-height:16px;">EPM<br>SERVICES</div>
  <div class="abs" style="left:110px;top:2847px;width:267px;height:186px;background:linear-gradient(135deg,#8c8f92,#5a5e62);box-shadow:0 2px 8px rgba(0,0,0,.2);border:4px solid #fff;" role="img" aria-label="Photo of a hand pointing at an evaluation screen with icons"></div>
  <div class="abs" style="left:337px;top:2726px;width:193px;height:270px;background:linear-gradient(160deg,#eef3f6,#b8d3e0);box-shadow:0 2px 8px rgba(0,0,0,.2);border:4px solid #fff;" role="img" aria-label="Photo of a laptop showing data analytics charts"></div>
  <div class="abs" style="left:346px;top:2850px;font-family:'Montserrat',sans-serif;font-weight:600;font-size:12px;line-height:16px;">DATA<br>ANALYTICS</div>

  <div class="heading abs" style="left:612px;top:2640px;font-size:35px;line-height:45px;">CONTACT US TO DISCUSS<br>YOUR BUSINESS NEEDS</div>
  <div class="field" style="top:2743px;height:45px;">Name</div>
  <div class="field" style="top:2794px;height:45px;">Email</div>
  <div class="field" style="top:2845px;height:45px;">Phone</div>
  <div class="field" style="top:2897px;height:122px;">Message</div>
  <div class="btn" style="left:612px;top:3028px;width:122px;height:40px;">SUBMIT NOW</div>

  <!-- footer -->
  <svg class="layer" width="1200" height="3589" viewBox="0 0 1200 3589">
    <path d="M0 3300 C300 3180 600 3130 800 3150 C1000 3170 1150 3260 1200 3300 V3589 H0Z" fill="var(--grey)"/>
    <path d="M0 3322 C300 3215 600 3180 800 3198 C1000 3215 1150 3275 1200 3310 V3589 H0Z" fill="var(--orange)"/>
    <path d="M0 3305 C300 3225 600 3215 800 3232 C1000 3250 1150 3310 1200 3330 V3589 H0Z" fill="var(--navy-deep)"/>
  </svg>

  <div class="foot-head" style="left:93px;">Quick Link</div>
  <div class="foot-list" style="left:93px;top:3352px;">
    <div>Home</div><div>Services</div><div>About Us</div><div>Contact Us</div>
  </div>

  <div class="foot-head" style="left:317px;">Contact Us</div>
  <div class="contact-row" style="top:3350px;">
    <div class="ico"><svg width="14" height="16" viewBox="0 0 14 16"><path d="M7 0a6 6 0 0 1 6 6c0 4-6 10-6 10S1 10 1 6a6 6 0 0 1 6-6z" fill="#fff"/><circle cx="7" cy="6" r="2.2" fill="var(--orange)"/></svg></div>
    <div>14 Harrow Lane, Millbrook,<br>Dublin 8, D08 K4T2</div>
  </div>
  <div class="contact-row" style="top:3405px;">
    <div class="ico"><svg width="14" height="14" viewBox="0 0 14 14"><path d="M3 1l2 3-1.3 1.3a8 8 0 0 0 5 5L10 9l3 2-1.5 2.5C6 13 1 8 .5 2.5Z" fill="#fff"/></svg></div>
    <div style="padding-top:3px;">01 555 0142</div>
  </div>
  <div class="contact-row" style="top:3440px;">
    <div class="ico"><svg width="14" height="11" viewBox="0 0 14 11"><rect x="0" y="0" width="14" height="11" rx="1" fill="#fff"/><path d="M1 1l6 5 6-5" fill="none" stroke="var(--orange)" stroke-width="1.4"/></svg></div>
    <div style="padding-top:3px;">info@corvane-solutions.com</div>
  </div>

  <div class="foot-head" style="left:674px;">Services</div>
  <div class="foot-list" style="left:674px;top:3353px;">
    <div>Advise &amp; Architect Services</div><div>Design &amp; Implement</div><div>Optimise &amp; Manage</div>
  </div>

  <div class="brand" style="left:922px;top:3340px;color:var(--white);font-size:16px;line-height:18px;">
    <div class="brand-dot" style="width:46px;height:46px;border-color:var(--white);"></div>
    <div>CORVANE<br>SOLUTIONS</div>
  </div>
  <div class="social" style="left:928px;" role="img" aria-label="Social profile link"></div>
  <div class="social" style="left:973px;" role="img" aria-label="Social profile link"></div>

  <div class="abs" style="left:0;width:1200px;top:3549px;text-align:center;color:var(--white);font-size:11px;">© 2022 <span style="color:var(--orange);">CORVANE SOLUTIONS</span>. All rights reserved</div>
</div>
</body>
</html>
```